Harbor Lantern Wellness Foundation branding and promotion

I need a brochure (not the typical trifold (maybe 5X5 with 5 or 6 segments). It needs to deliver several strong points: who we are, why we exist, what we do, how we do it, and DONATE now.We are a fairly new Foundation in the Veteran space, a very crowded space. I need a design that will separate us and clearly state: who we are (our story), what we do, how we do it and why. Our website is www.hlwf-sample.us

Target Market(s)

Corporate America, Veterans, their family members, the members of the community where they live, work, play and pray

Font styles to use
Serif

Colors
ffc214
faa54b
f68d4d
e34197

Requirements
Must have
• "CURB APPEAL", it must grab the target market and COMPEL them to volunteer, donate, sponsor foundation activities.
• Pictures
• Graphics
• Review website for content, I will then expand, edit, etc.
Nice to have
• For colors, see the colors in the logo. Other complementary colors can be used

```html
<!DOCTYPE html>
<html lang="en">
<head>
<meta charset="utf-8">
<title>Harbor Lantern Wellness Foundation Brochure</title>
<link href="https://fonts.googleapis.com/css2?family=Source+Sans+3:wght@400;600;700&family=Oswald:wght@500&display=swap" rel="stylesheet">
<style>
:root{
  --red:#b8262b;
  --red-deep:#a3201f;
  --orange:#e8722c;
  --orange-light:#f68d4d;
  --peach:#faa54b;
  --yellow:#f6a81b;
  --gold:#ffc214;
  --grey:#5f6062;
  --ink:#3a3a3c;
  --paper:#ffffff;
  --stage:#ececec;
}
*{box-sizing:border-box;margin:0;padding:0}
html,body{width:1200px;height:910px;overflow:hidden;background:var(--stage);font-family:"Source Sans 3",Arial,sans-serif;color:var(--ink)}
.spread{position:absolute;left:30px;width:1140px;height:381px;display:flex;box-shadow:0 6px 14px rgba(0,0,0,.25)}
.spread--outside{top:54px}
.spread--inside{top:475px}
.panel{position:relative;width:380px;height:381px;overflow:hidden;background:var(--paper)}
.panel + .panel{border-left:1px solid rgba(0,0,0,.08)}
.photo{position:absolute}
.abs{position:absolute}
svg.shape{position:absolute;left:0;top:0}

.brand{position:absolute;display:flex;align-items:center;gap:6px;color:var(--grey);font-size:12.5px;font-weight:400;line-height:1.05;text-align:right}
.brand__dot{width:16px;height:16px;border-radius:50%;background:var(--orange);flex:none}

.tag{position:absolute;left:0;height:19px;padding:0 30px 0 20px;color:#fff;font-weight:700;font-size:11px;line-height:19px;clip-path:polygon(0 0,100% 0,calc(100% - 10px) 100%,0 100%)}
.tag--red{background:var(--red)}
.tag--orange{background:var(--orange)}
.copy{position:absolute;left:20px;right:18px;font-size:8.4px;line-height:1.38;text-align:justify}
.copy p + p{margin-top:9px}

.url-band{position:absolute;left:0;right:0;top:338px;height:22px;background:var(--yellow);color:#fff;font-weight:700;font-size:14px;letter-spacing:1.6px;text-align:center;line-height:22px}
.contact{position:absolute;left:0;right:0;top:360px;height:21px;background:var(--red-deep);color:#fff;font-size:8.5px;text-align:center;line-height:21px}

.donate{position:absolute;width:78px;height:78px;border-radius:50%;background:var(--orange);border:3px solid #f39a4c;box-shadow:0 0 0 2px var(--orange);display:flex;align-items:center;justify-content:center;font-family:"Oswald",Impact,sans-serif;font-size:18px;color:#ffe0a8;letter-spacing:.5px}

.promise{position:absolute;right:18px;text-align:right;color:#fff}
.promise__lead{font-weight:700;font-size:11px;line-height:1.6;text-transform:uppercase}
.promise__join{font-size:8.5px;line-height:1.35;margin-top:10px}

.tagline{position:absolute;top:25px;left:10px;right:10px;color:#fff;font-weight:600;font-size:13px;letter-spacing:1.2px;text-align:center;line-height:1.45}

.story-head{position:absolute;left:20px;top:32px;color:#fff;font-weight:700;font-size:14px}
.pillar-icon{position:absolute;left:20px;width:56px;height:56px;border-radius:50%;background:var(--yellow);border:4px solid #fff;box-shadow:0 2px 4px rgba(0,0,0,.25)}
.pillar-icon::after{content:"";position:absolute;inset:9px;border-radius:50%;background:var(--orange)}
.pillar{position:absolute;left:90px;right:14px;font-size:8.4px;line-height:1.3;text-align:justify}
.pillar h3{color:var(--red);font-size:11.5px;font-weight:700;margin-bottom:2px;text-align:left}
.bullets{list-style:none}
.bullets li{position:relative;padding-left:13px;margin-bottom:3px;line-height:1.2;text-align:left}
.bullets li::before{content:"";position:absolute;left:0;top:2px;width:7px;height:7px;border-radius:50%;background:var(--red)}

.panel--support{background:linear-gradient(180deg,var(--orange) 0%,#f08a3a 55%,var(--yellow) 75%,var(--gold) 100%)}
.support-tag{position:absolute;left:120px;top:20px;width:156px;height:18px;background:var(--red);color:#fff;font-weight:700;font-size:11px;text-align:center;line-height:18px}
.support-topics{position:absolute;top:45px;left:0;right:0;text-align:center;color:var(--red-deep);font-size:8.5px;line-height:1.35}
.support-head{position:absolute;top:87px;left:0;right:0;text-align:center;color:#fff;font-weight:700;font-size:10.5px}
.facts{position:absolute;top:110px;left:18px;right:16px;list-style:none;color:#fff;font-size:8.4px;line-height:1.3}
.facts li{position:relative;padding-left:12px;margin-bottom:9px}
.facts li::before{content:"";position:absolute;left:0;top:1px;width:7px;height:7px;border-radius:50%;border:1.5px solid var(--gold)}
.thumbs{position:absolute;top:235px;left:12px;right:12px;display:flex;gap:9px}
.thumbs .photo{position:relative;flex:1;height:80px;border:2px solid #f7b24a}
.support-join{position:absolute;top:328px;left:0;right:0;text-align:center;color:#fff;font-size:8.5px;line-height:1.35}
.url-pill{position:absolute;top:350px;left:115px;width:152px;height:18px;border-radius:9px;background:#fff;color:var(--yellow);font-weight:700;font-size:11px;letter-spacing:1px;text-align:center;line-height:18px}

.care-bar{position:absolute;left:0;top:208px;width:310px;height:17px;background:var(--red);color:#fff;font-weight:700;font-size:10px;padding-left:20px;line-height:17px;clip-path:polygon(0 0,100% 0,calc(100% - 14px) 100%,0 100%)}
.care-sub{position:absolute;left:20px;right:10px;top:230px;color:var(--orange);font-size:9px}
.care-copy{position:absolute;left:20px;right:16px;top:254px;font-size:8.5px;line-height:1.4;color:var(--ink)}
.care-box{position:absolute;left:20px;top:310px;width:300px;height:50px;background:var(--orange);border-radius:3px;color:#fff;font-size:8.4px;line-height:1.35;padding:6px 40px 0 8px}
</style>
</head>
<body>

<section class="spread spread--outside">
  <!-- Who we are -->
  <article class="panel panel--about" style="background:linear-gradient(90deg,#fff 80%,#e9e9e9 100%)">
    <div class="brand" style="right:20px;top:10px"><span class="brand__dot"></span><span>Harbor Lantern<br>Wellness Foundation</span></div>
    <div class="tag tag--red" style="top:46px;width:190px">WHO WE ARE</div>
    <div class="copy" style="top:78px">
      <p>Having devoted their lives to serving our country and defending our freedom, Veterans leave military service with a host of potentially debilitating health conditions, many remaining unknown or dormant for years after discharge or retirement. Harbor Lantern Wellness Foundation (HLWF), a non-profit 501c3 charitable entity, was established in 2013 by military veterans with over 70 years of experience and expertise in the health and healthcare arena for the express purpose of addressing systemic inequities regarding access to and quality of care for Veterans and their families.</p>
      <p>In addition, HLWF works tirelessly to ensure Veterans, their families and the communities where they live, work, play, prayare connected, educated, trained to appropriately align integrated healthcare, support services and community advocacy</p>
    </div>
    <div class="tag tag--orange" style="top:219px;width:190px">OUR MISSION</div>
    <div class="copy" style="top:250px">
      <p>Harbor Lantern Wellness Foundation is committed to help and to give back to the men, women and families who serve our nation – whether in uniform or not, at home or abroad, and in times of turmoil or peace.</p>
      <p>Making good America's promise…your promise… to ensure they get the quality healthcare is a way to operationalize <b>"Thank You for Your Service".</b></p>
    </div>
    <div class="url-band">www.hlwf-sample.us</div>
  </article>

  <!-- Front cover -->
  <article class="panel panel--cover">
    <div class="photo" role="img" aria-label="Three smiling veterans in caps and uniforms standing together" style="left:0;top:0;width:380px;height:338px;background:linear-gradient(135deg,#6f7a52 0%,#a9a592 40%,#4d4b46 100%)"></div>
    <svg class="shape" width="380" height="338" viewBox="0 0 380 338" aria-hidden="true">
      <defs>
        <linearGradient id="coverOrange" x1="0" y1="0" x2="1" y2="1">
          <stop offset="0" stop-color="#f29a45"/><stop offset="1" stop-color="#c9451f"/>
        </linearGradient>
      </defs>
      <polygon points="0,165 0,338 168,338" fill="#fff"/>
      <polygon points="380,70 380,338 160,338" fill="url(#coverOrange)"/>
    </svg>
    <div class="brand" style="left:8px;top:232px"><span class="brand__dot"></span><span>Harbor Lantern<br>Wellness Foundation</span></div>
    <div class="donate" style="left:272px;top:152px">DONATE</div>
    <div class="promise" style="top:240px">
      <div class="promise__lead">We will always remember<br>and we will always be there,<br>just as you have been for us</div>
      <div class="promise__join">Join forces with the Harbor Lantern<br>Wellness Foundation and be a CHAMPION<br>to our Heroes and their Families</div>
    </div>
    <div class="url-band">www.hlwf-sample.us</div>
    <div class="contact">555. 010. 2741 &nbsp;|&nbsp; 88 Beacon Row, Suite 210 Fairhaven, MD 20000</div>
  </article>

  <!-- Back panel -->
  <article class="panel panel--family" style="background:linear-gradient(160deg,#f5a24a,#e46c2a)">
    <div class="photo" role="img" aria-label="Smiling family of a father, mother and two young children outdoors" style="left:0;top:80px;width:380px;height:301px;background:linear-gradient(135deg,#7d8f4c 0%,#b7a17a 45%,#4a5a6d 100%)"></div>
    <svg class="shape" width="380" height="381" viewBox="0 0 380 381" aria-hidden="true">
      <polygon points="0,0 380,0 380,45 0,80" fill="#ee8a3a"/>
      <polygon points="380,45 380,165 190,165" fill="#fff"/>
    </svg>
    <div class="tagline">…HEALTHY AND WELL LIVES UNDIMINISHED BY<br>SERVICE RELATED HEALTH CONCERNS…</div>
    <div class="brand" style="right:12px;top:108px"><span class="brand__dot"></span><span>Harbor Lantern<br>Wellness Foundation</span></div>
    <div class="url-band" style="background:rgba(246,168,27,.92)">www.hlwf-sample.us</div>
    <div class="donate" style="left:290px;top:300px">DONATE</div>
  </article>
</section>

<section class="spread spread--inside">
  <!-- Our story -->
  <article class="panel panel--story" style="background:linear-gradient(90deg,#fff 82%,#ececec 100%)">
    <svg class="shape" width="380" height="120" viewBox="0 0 380 120" aria-hidden="true">
      <defs>
        <linearGradient id="storyOrange" x1="0" y1="0" x2="1" y2="1">
          <stop offset="0" stop-color="#e8722c"/><stop offset="1" stop-color="#f6a04a"/>
        </linearGradient>
      </defs>
      <polygon points="0,0 225,0 0,110" fill="url(#storyOrange)"/>
    </svg>
    <div class="story-head">OUR STORY</div>
    <div class="brand" style="right:20px;top:22px"><span class="brand__dot"></span><span>Harbor Lantern<br>Wellness Foundation</span></div>
    <div class="pillar-icon" style="top:66px"></div>
    <div class="pillar" style="top:72px">
      <h3>PURPOSE</h3>
      <p>Make good on America's promise "To care for those who shall have borne the battle." (adapted from a wartime address)</p>
    </div>
    <div class="pillar-icon" style="top:134px"></div>
    <div class="pillar" style="top:144px">
      <h3>VISION</h3>
      <p>HLWF envisions a world in which ALL veterans and their families live healthy and well lives undiminished by their service related health concerns</p>
    </div>
    <div class="pillar-icon" style="top:202px"></div>
    <div class="pillar" style="top:212px">
      <h3>STRATEGY</h3>
      <ul class="bullets">
        <li>Amplify the veteran community voice in their battle for health and wellness</li>
        <li>Facilitate the advocation of equitable healthcare for veterans and their families</li>
        <li>Develop, gather and disseminate information and education regarding veterans' health, healthcare and wellness to veterans, their families and the communities in which they live</li>
        <li>Develop, implement and evaluate education and training designed for healthcare professionals that facilitates and enhances their understanding of the unique health and wellness needs of veterans and their families</li>
        <li>Continuously refine the Veteran Care Circle model to safeguard the mission.</li>
      </ul>
    </div>
  </article>

  <!-- Support -->
  <article class="panel panel--support">
    <div class="support-tag">SUPPORT OUR MISSION</div>
    <div class="support-topics">Community Health and Wellness Healthcare Education<br>Health and Wellness<br>Engagement Events and Training Forums</div>
    <div class="support-head">The numbers of Veterans and their families in need of help are substantial</div>
    <ul class="facts">
      <li>20 million discharged American warriors are either currently suffering multiple chronic conditions brought on by the circumstances of their military service or are at risk.</li>
      <li>42 million family members are also affected.</li>
      <li>62 million total number of those needing some form of specialized care.</li>
      <li>These 62 million Americans represent about 25% of the entire U.S. population in need of some form of specialized or unique care.</li>
    </ul>
    <div class="thumbs">
      <div class="photo" role="img" aria-label="Group of people at a community health event" style="background:linear-gradient(135deg,#5d7fa3,#c59a7a)"></div>
      <div class="photo" role="img" aria-label="Speaker presenting to a training class" style="background:linear-gradient(135deg,#3e4a52,#8d9aa0)"></div>
      <div class="photo" role="img" aria-label="Town hall meeting in a community room" style="background:linear-gradient(135deg,#c9ced3,#7e8890)"></div>
    </div>
    <div class="support-join">Join Forces with the Harbor Lantern Wellness Foundation and<br>be a CHAMPION for our Heroes and their Families</div>
    <div class="url-pill">www.hlwf-sample.us</div>
  </article>

  <!-- Children of veterans -->
  <article class="panel panel--care">
    <div class="photo" role="img" aria-label="Nurse with stethoscope caring for a mother and young daughter in a clinic" style="left:0;top:0;width:380px;height:210px;background:linear-gradient(135deg,#8a7664 0%,#cfc7c0 50%,#8e9aa6 100%)"></div>
    <svg class="shape" width="380" height="210" viewBox="0 0 380 210" aria-hidden="true">
      <polygon points="160,0 380,0 380,120" fill="#e8722c" opacity=".85"/>
      <polygon points="250,0 380,0 380,55" fill="#b8262b"/>
    </svg>
    <div class="care-bar">Quality Care for Children of Veterans</div>
    <div class="care-sub">Military children have more healthcare needs, but less access and lower quality</div>
    <div class="care-copy">Children in military families insured by ShieldCare are more likely to have special health care needs, and more likely to have a behavioral health diagnosis compared to their civilian peers, according to a new study.</div>
    <div class="care-box">Veteran families are also affected. This brings the number of those needing some form of specialized care to around 75 million, representing about 25% of the entire U.S. population</div>
    <div class="donate" style="left:296px;top:290px">DONATE</div>
  </article>
</section>

</body>
</html>
```